Bravik Telecom Branding and Visual Identity Project

We need some visual identity items for Bravik Telecom, which should be produced based on the company's logo attached.

I would like the brochure to be as lightweight as possible so that it can be sent via email.

Below are the items we need to be made.

- Company letterhead
- Company brochure in PDF format (single page)
- Email signature (only one)
- Wallpaper
- Banner for use on social media
- Customized shirt

Target Market(s)

Passengers and crew members of ships

Industry/Entity Type

Telecom & Maritime

Colors
0054AA
0677BA
7BADD7
CADEEF
E8F1F8

Requirements
Nice to have
• Colors that match the logo
Should not have
• Colors that clash with the logo colors

```html
<!DOCTYPE html>
<html lang="en">
<head>
<meta charset="utf-8">
<title>Bravik Telecom Flyer</title>
<link href="https://fonts.googleapis.com/css2?family=Red+Hat+Display:wght@700&family=Didact+Gothic&family=Montserrat:wght@400&display=swap" rel="stylesheet">
<style>
  :root {
    --brand-blue: #0a6cb9;
    --deep-blue: #0054aa;
    --band-blue: #0a72c0;
    --photo-dark: #173f6b;
    --photo-mid: #2f6aa0;
    --photo-light: #b9d2ea;
    --paper: #f7f7f7;
    --text-grey: #555b61;
    --body-grey: #7a7f85;
    --stage: #dedede;
  }
  * { margin: 0; padding: 0; box-sizing: border-box; }
  html, body { width: 1153px; height: 1200px; overflow: hidden; background: var(--stage); }
  .flyer {
    position: absolute; left: 168px; top: 30px;
    width: 1008px; height: 1406px;
    background: var(--paper);
    transform: scale(0.811); transform-origin: top left;
    font-family: "Didact Gothic", sans-serif;
  }
  .brand-name {
    position: absolute; left: 82px; top: 128px;
    font-family: "Red Hat Display", sans-serif; font-weight: 700;
    font-size: 50px; color: var(--brand-blue); letter-spacing: 0.5px;
  }
  .headline {
    position: absolute; left: 568px; top: 68px;
    font-family: "Red Hat Display", sans-serif; font-weight: 700;
    font-size: 49px; line-height: 57px; color: var(--brand-blue);
  }
  .hero { position: absolute; left: 0; top: 274px; width: 1008px; height: 710px; }
  .hero svg { display: block; }
  .services-title, .history-title {
    position: absolute;
    font-family: "Red Hat Display", sans-serif; font-weight: 700;
    color: var(--brand-blue); font-size: 33px;
  }
  .services-title { left: 75px; top: 1020px; }
  .services-list {
    position: absolute; left: 74px; top: 1068px; width: 880px;
    list-style: none; font-size: 24px; line-height: 35px; color: var(--text-grey);
    display: flex; flex-wrap: wrap;
  }
  .services-list li { margin-right: 10px; white-space: nowrap; }
  .services-list li::before {
    content: ""; display: inline-block; width: 12px; height: 12px;
    background: var(--brand-blue); margin-right: 11px; vertical-align: 2px;
  }
  .services-list .row-break { flex-basis: 100%; height: 0; margin: 0; }
  .services-list .row-break::before { display: none; }
  .portrait {
    position: absolute; left: 74px; top: 1188px; width: 97px; height: 122px;
    background: linear-gradient(160deg, #9a9a9a, #3d3d3d);
  }
  .history-title { left: 192px; top: 1178px; }
  .history-text {
    position: absolute; left: 192px; top: 1228px; width: 780px;
    font-size: 13px; line-height: 18px; color: var(--body-grey);
  }
  .contact-band {
    position: absolute; left: 0; top: 1345px; width: 1008px; height: 61px;
    background: var(--band-blue); color: #fff;
    font-family: "Montserrat", sans-serif; font-size: 35px; letter-spacing: 1px;
    display: flex; align-items: center; padding-left: 84px; gap: 12px;
  }
  .contact-band svg { flex: none; }
</style>
</head>
<body>
  <main class="flyer">
    <div class="brand-name">Bravik Telecom</div>
    <h1 class="headline">Get Flexible,<br>Future-Built<br>Telecom Systems</h1>

    <div class="hero">
      <svg width="1008" height="710" viewBox="0 0 1008 710">
        <defs>
          <linearGradient id="heroTone" x1="0" y1="0" x2="1" y2="1">
            <stop offset="0" stop-color="#1c4a7c"/>
            <stop offset="0.55" stop-color="#3c6e9c"/>
            <stop offset="1" stop-color="#a9c6e2"/>
          </linearGradient>
        </defs>
        <rect role="img" aria-label="Photo of a smiling support agent wearing a headset in a bright office, a colleague working behind him" width="1008" height="710" fill="url(#heroTone)"/>
        <polygon class="accent-wedge" points="0,0 200,0 336,333 176,710 0,300" fill="#0a5fae" opacity="0.78"/>
        <polygon class="accent-wedge" points="715,0 1008,0 1008,710 1000,710" fill="#0a5fae" opacity="0.85"/>
      </svg>
    </div>

    <h2 class="services-title">Products &amp; Services</h2>
    <ul class="services-list">
      <li>SIP Trunking</li>
      <li>Corvix Hosted PBX</li>
      <li>Corvix Licensing</li>
      <li>Fax Over IP</li>
      <li class="row-break"></li>
      <li>SMS Text Messaging</li>
      <li>International &amp; Toll-Free Phone Numbers</li>
    </ul>

    <div class="portrait" role="img" aria-label="Black and white portrait of a bearded inventor"></div>
    <h2 class="history-title">A bit of history...</h2>
    <p class="history-text">Did you know that Edmund Harlow, the inventor of the telephone, used and recommended the use of “Ahoy” as the standard telephone greeting before “Hello”, later suggested by Walter Pryce, became the norm? “Ahoy” has been used in the English language since the mid-1700s and extends well beyond its nautical use. Ahoy! We look forward to working with you.</p>

    <footer class="contact-band">
      <svg width="30" height="30" viewBox="0 0 24 24" fill="none" stroke="#fff" stroke-width="1.6" stroke-linejoin="round">
        <path d="M5 3h4l2 5-2.5 1.5a11 11 0 0 0 6 6L16 13l5 2v4a2 2 0 0 1-2 2A17 17 0 0 1 3 5a2 2 0 0 1 2-2z"/>
      </svg>
      <span>(855)410-3386</span>
      <svg width="32" height="24" viewBox="0 0 32 24" fill="none" stroke="#fff" stroke-width="2">
        <rect x="2" y="3" width="28" height="18"/><path d="M2 3l14 11L30 3M2 21l10-9M30 21l-10-9"/>
      </svg>
      <span>sales@braviktelecom.example</span>
    </footer>
  </main>
</body>
</html>
```